Letterhead and matching envelope design for a dental office

We need a new stationary design, letterhead and envelope #10, for a dental office in Denver area. We are called Brightcove Dental. We want a simple and minimalistic design but not a boring design. I wish to have one good point that makes it look professional. I have attached our logo. Feel free to use either one. I want the design for letterhead and envelope look like a "matching pair" but not look the same. The envelope doesn't have to be white and it will have an address window on bottom left.

Target Market(s)

everyone who visits dentist (adults)

Industry/Entity Type

Dental

Font styles to use
Other font styles liked:
• close to font on logo or something that matches well

Requirements
Must have
• professional
• simple, minimalistic
• unique point that stands out
Nice to have
• matching but not same design for letterhead and envelope
Should not have
• not look like all the other boring designs
• no flowery, distracting feats

```html
<!DOCTYPE html>
<html lang="en">
<head>
<meta charset="utf-8">
<title>Brightcove Dental — Letterhead &amp; Envelope</title>
<link href="https://fonts.googleapis.com/css2?family=Libre+Baskerville&family=Arimo&display=swap" rel="stylesheet">
<style>
  :root {
    --backdrop: #2f2f2f;
    --paper: #ffffff;
    --brand-green: #3bb54a;
    --green-pale: #d7eedb;
    --green-soft: #a0dca6;
    --green-mid: #72c97a;
    --env-pale: #c5e8c9;
    --footer-ink: #3d3d3d;
    --serif: "Libre Baskerville", "Times New Roman", serif;
    --sans: "Arimo", Arial, sans-serif;
  }
  html, body {
    margin: 0;
    padding: 0;
    width: 710px;
    height: 1200px;
    overflow: hidden;
    background: var(--backdrop);
  }
  .canvas {
    position: relative;
    width: 710px;
    height: 1200px;
  }
  .sheet {
    position: absolute;
    background: var(--paper);
    overflow: hidden;
  }
  .sheet .wedges {
    position: absolute;
    inset: 0;
    width: 100%;
    height: 100%;
  }

  /* Letterhead */
  .letterhead { left: 54px; top: 24px; width: 602px; height: 780px; }
  .letterhead .brand-dot {
    position: absolute; left: 98px; top: 40px;
    width: 44px; height: 44px; border-radius: 50%;
    background: var(--brand-green);
  }
  .letterhead .wordmark {
    position: absolute; left: 200px; top: 38px; width: 400px;
    text-align: center;
    font-family: var(--serif);
    font-variant: small-caps;
    font-size: 29px;
    letter-spacing: 1.5px;
    color: var(--brand-green);
    margin: 0;
    line-height: 1;
  }
  .letterhead .location {
    position: absolute; left: 200px; top: 74px; width: 400px;
    text-align: center;
    font-family: var(--serif);
    font-size: 14px;
    letter-spacing: 9px;
    color: var(--brand-green);
    margin: 0;
  }
  .letterhead .contact-footer {
    position: absolute; left: 18px; right: 18px; top: 750px;
    display: flex; justify-content: space-between;
    font-family: var(--sans);
    font-size: 9.5px;
    color: var(--footer-ink);
    white-space: pre;
  }

  /* Envelope */
  .envelope { left: 18px; top: 872px; width: 674px; height: 292px; }
  .envelope .brand-dot {
    position: absolute; left: 68px; top: 19px;
    width: 28px; height: 28px; border-radius: 50%;
    background: var(--brand-green);
  }
  .envelope .wordmark {
    position: absolute; left: 139px; top: 24px;
    font-family: var(--serif);
    font-variant: small-caps;
    font-size: 14px;
    letter-spacing: 0.8px;
    color: var(--brand-green);
    margin: 0;
    line-height: 1;
  }
  .envelope .return-address {
    position: absolute; left: 162px; top: 40px;
    font-family: var(--sans);
    font-size: 7px;
    line-height: 9px;
    color: var(--brand-green);
    font-style: normal;
    white-space: pre;
  }
</style>
</head>
<body>
<main class="canvas">

  <section class="sheet letterhead" aria-label="Letterhead">
    <svg class="wedges" viewBox="0 0 602 780" preserveAspectRatio="none" aria-hidden="true">
      <polygon points="0,780 602,298 602,780" fill="var(--green-pale)"/>
      <polygon points="0,780 602,441 602,780" fill="var(--green-soft)"/>
      <polygon points="0,780 602,566 602,780" fill="var(--green-mid)"/>
    </svg>
    <span class="brand-dot" aria-hidden="true"></span>
    <h1 class="wordmark">Brightcove Dental</h1>
    <p class="location">Lakeridge</p>
    <footer class="contact-footer">
      <span>4210 ALDER CREEK DR  SUITE 210  LAKERIDGE CO 80031</span>
      <span>(720) 555-0147</span>
      <span>WWW.BRIGHTCOVEDENTAL.COM</span>
    </footer>
  </section>

  <section class="sheet envelope" aria-label="Envelope">
    <svg class="wedges" viewBox="0 0 674 292" preserveAspectRatio="none" aria-hidden="true">
      <polygon points="0,292 674,0 674,292" fill="var(--env-pale)"/>
      <polygon points="0,292 674,98 674,292" fill="var(--green-mid)"/>
      <polygon points="0,292 674,195 674,292" fill="var(--brand-green)"/>
    </svg>
    <span class="brand-dot" aria-hidden="true"></span>
    <h2 class="wordmark">Brightcove Dental</h2>
    <address class="return-address">4210 ALDER CREEK DR  SUITE 210
LAKERIDGE  CO  80031</address>
  </section>

</main>
</body>
</html>
```